BrightHaven is the name of the business, it is a disability service where we offer

Assist-Life Stage, Transition

Household Tasks

Group/Centre Activities

Support Coordination

Innov Community Participation

Home Modification

Participate Community

Assist Personal Activities

Community Nursing Care

Development-Life Skills

Personal Activities High

Assist-Travel/Transport

Assist Access/Maintain Employ

Daily Tasks/Shared Living

Assist Prod-Pers Care/Safety

Assistive Prod-Household Task

Hi, I have uploaded the pictures and short clips. please make them look cohesive and professional I trust you and seen your previous work. many thanks

Target Market(s)

Everyone

Coding

Coded - Design and coding required

Number of Pages Required

2 page

Requirements
Must have
• must be inviting and warm. this is for a disability service that I am passionate about and work from my heart. it must state all the services I offer and contact details. I have attached my Logo
• contact number 0461839207
• once I have a facebook page and a insta and snapchat is then ok to add them because I don't have any social media right now.

```html
<!DOCTYPE html>
<html lang="en">
<head>
<meta charset="utf-8">
<title>BrightHaven – Disability Services</title>
<link href="https://fonts.googleapis.com/css2?family=Lato:wght@300;400;700&display=swap" rel="stylesheet">
<style>
:root{
  --green:#8cc63f;
  --green-dark:#6fb52c;
  --teal:#1a9b7b;
  --teal-deep:#14927f;
  --ink:#1d1d1d;
  --text:#444;
  --muted:#8a8a8a;
  --soft-bg:#efefef;
  --bar-bg:#dcdcdc;
  --white:#fff;
  --link:#2a58c7;
}
*{box-sizing:border-box;margin:0;padding:0}
html,body{width:1200px;height:2643px;overflow:hidden}
body{position:relative;font-family:'Lato',sans-serif;color:var(--text);background:var(--white)}
.abs{position:absolute}

/* header */
.site-header{left:0;top:0;width:1200px;height:92px;background:var(--white)}
.brand{display:flex;align-items:center;gap:12px}
.brand-dot{width:46px;height:46px;border-radius:50%;background:var(--teal)}
.brand-name{font-size:38px;font-weight:400;color:var(--teal);letter-spacing:.2px}
.site-header .brand{position:absolute;left:181px;top:20px}
.main-nav{position:absolute;left:522px;top:37px;display:flex;gap:0}
.main-nav a{position:absolute;white-space:nowrap;font-size:17px;color:var(--teal);text-decoration:none}
.main-nav a.active{color:var(--green)}

/* hero */
.hero{left:0;top:92px;width:1200px;height:580px;overflow:hidden}
.hero-photo{position:absolute;inset:0;background:linear-gradient(90deg,#8b8577 0%,#b7ada0 30%,#e6e4df 60%,#f4f4f2 100%)}
.hero-copy{position:absolute;left:652px;top:128px;width:420px}
.hero-title{font-size:42px;font-weight:400;line-height:1.02;color:var(--ink)}
.hero-title span{display:block;color:var(--teal)}
.hero-rule{width:58px;height:4px;background:var(--green);margin:10px 0 14px 4px}
.hero-copy p{font-size:19px;line-height:1.3;color:#555}
.btn{display:inline-flex;align-items:center;justify-content:center;border-radius:24px;background:var(--green);color:var(--white);font-size:18px;font-weight:700;text-decoration:none}
.hero-copy .btn{margin-top:28px;width:156px;height:46px}
.hero-next{position:absolute;left:1060px;top:190px}

/* about */
.about-copy{left:189px;top:738px;width:450px}
.about-copy h2{font-size:38px;font-weight:400;color:var(--ink)}
.about-lead{margin-top:24px;font-size:18px;line-height:1.3;color:#333}
.about-body{margin-top:18px;font-size:15px;line-height:1.5;color:var(--muted)}
.about-copy .btn{margin-top:24px;width:160px;height:44px}
.about-emblem{left:655px;top:687px;width:344px;height:344px;border-radius:50%;background:radial-gradient(circle at 50% 40%,#9ccf4a 0%,#3aa36a 55%,#16907b 100%);display:flex;align-items:center;justify-content:center}
.about-emblem span{font-size:34px;color:var(--white)}

/* services */
.services-waves{left:0;top:1095px}
.services{left:0;top:1180px;width:1200px;height:600px;background:linear-gradient(160deg,#84c43a 0%,#4cb15a 50%,#17997c 100%)}
.services-bottom{left:0;top:1755px}
.services h2{position:absolute;left:0;width:1200px;top:74px;text-align:center;font-size:34px;font-weight:400;color:var(--white)}
.service{position:absolute;width:300px;display:flex;gap:10px;color:var(--white)}
.service-icon{flex:none;width:78px;height:78px;border-radius:50%;background:rgba(255,255,255,.22);display:flex;align-items:center;justify-content:center}
.service h3{font-size:21px;font-weight:400;line-height:1.22}
.service p{margin-top:6px;font-size:12.5px;line-height:1.55;opacity:.95;width:190px}
.btn-outline{position:absolute;left:551px;top:522px;width:145px;height:44px;border:2px solid var(--white);border-radius:24px;color:var(--white);font-size:18px;display:flex;align-items:center;justify-content:center}

/* blog */
.blog{left:0;top:1815px;width:1200px;height:502px;background:var(--soft-bg)}
.blog h2{position:absolute;left:180px;top:82px;font-size:32px;font-weight:400;color:var(--ink)}
.post{position:absolute;top:146px;width:262px;height:296px;background:var(--white);border:1px solid #b9b9b9}
.post-photo{height:164px}
.post-date{position:absolute;left:9px;top:176px;width:51px;height:51px;border-radius:50%;background:var(--green);color:var(--white);text-align:center;line-height:1}
.post-date b{display:block;font-size:20px;font-weight:400;margin-top:9px}
.post-date small{font-size:11px}
.post h3{position:absolute;left:68px;top:182px;font-size:16px;font-weight:400;color:var(--ink)}
.post p{position:absolute;left:68px;top:206px;width:180px;font-size:10.5px;line-height:1.5;color:#666}
.post a{position:absolute;left:68px;top:262px;font-size:12px;font-weight:700;color:var(--link);text-decoration:none}

/* footer */
.site-footer{left:0;top:2317px;width:1200px;height:273px}
.site-footer .brand{position:absolute;left:189px;top:86px}
.footer-col{position:absolute;top:72px}
.footer-col h4{font-size:20px;font-weight:400;color:var(--ink)}
.footer-col ul{list-style:none;margin-top:14px}
.footer-col li{font-size:13px;color:#666;height:26.5px}
.signup-note{margin-top:12px;font-size:13px;color:#555}
.signup{margin-top:10px;width:195px;height:28px;border:1px solid #aaa;border-radius:3px;background:#e9e9e9;display:flex;align-items:center;justify-content:space-between;padding:0 8px 0 12px;font-size:11px;color:#888}
.socials{display:flex;gap:4px;margin-top:14px}
.socials span{width:33px;height:33px;border-radius:50%;border:2px solid var(--teal)}
.copyright{left:0;top:2590px;width:1200px;height:53px;background:var(--bar-bg);text-align:center;line-height:53px;font-size:12px;color:#555}
</style>
</head>
<body>

<header class="site-header abs">
  <div class="brand"><span class="brand-dot"></span><span class="brand-name">BrightHaven</span></div>
  <nav class="main-nav">
    <a class="active" style="left:0">Home</a>
    <a style="left:68px">About Us</a>
    <a style="left:160px">Services</a>
    <a style="left:244px">Blogs</a>
    <a style="left:310px">Testimonials</a>
    <a style="left:422px">Contact Us</a>
  </nav>
</header>

<section class="hero abs">
  <div class="hero-photo" role="img" aria-label="Photo of a carer and a man in a wheelchair sharing a high five in a bright office"></div>
  <div class="hero-copy">
    <h1 class="hero-title">We Provide<span>Disability Services</span></h1>
    <div class="hero-rule"></div>
    <p>Morbi eget arcu Morbi porta libero id ullam corper nonummy nibh ligula</p>
    <a class="btn">Contact Us</a>
  </div>
  <svg class="hero-next" width="30" height="64" viewBox="0 0 30 64"><path d="M3 2 L27 32 L3 62" fill="none" stroke="#888" stroke-width="2"/></svg>
  <svg class="abs" style="left:0;top:460px" width="1200" height="120" viewBox="0 0 1200 120">
    <path d="M0 58 C250 40 420 85 620 58 C820 30 1000 10 1200 40 L1200 120 L0 120Z" fill="var(--teal)"/>
    <path d="M0 75 C250 62 420 112 640 90 C860 70 1000 30 1200 52 L1200 120 L0 120Z" fill="var(--green)"/>
    <path d="M0 82 C250 74 420 122 640 102 C860 84 1000 50 1200 66 L1200 120 L0 120Z" fill="var(--white)"/>
  </svg>
</section>

<section class="about-copy abs">
  <h2>About BrightHaven</h2>
  <p class="about-lead">Morbi eget arcu Morbi porta libero id ullamcorper nonummy nibh ligula pulvinar metus eget</p>
  <p class="about-body">Vivamus porttitor purus nisi eleifend libero a tempus libero lectus feugiat felis Morbi diam mauris viverra in gravida eu mattis in ante Morbi eget arcu Morbi porta libero id ullamcorper</p>
  <a class="btn">Contact Us</a>
</section>
<div class="about-emblem abs"><span>BrightHaven</span></div>

<svg class="services-waves abs" width="1200" height="100" viewBox="0 0 1200 100">
  <path d="M0 40 C120 5 260 20 420 60 C560 95 700 70 820 50 C960 30 1100 40 1200 35 L1200 100 L0 100Z" fill="var(--teal)"/>
  <path d="M0 62 C140 30 280 50 430 82 C560 105 700 82 820 64 C960 48 1100 55 1200 50 L1200 100 L0 100Z" fill="var(--white)"/>
  <path d="M0 80 C140 55 290 72 440 95 C580 110 720 92 840 72 C980 58 1100 62 1200 60 L1200 100 L0 100Z" fill="#82c33b"/>
</svg>

<section class="services abs">
  <h2>Our Services</h2>
  <div class="service" style="left:171px;top:172px"><span class="service-icon"></span><div><h3>Assist-Life Stage,<br>Transition</h3><p>elementum elit at tellus nec ultricies sit amet porttitor mattis</p></div></div>
  <div class="service" style="left:470px;top:172px"><span class="service-icon"></span><div><h3>Household Tasks</h3><p>elementum elit at tellus nec ultricies sit amet porttitor mattis enim In massa libero interdu</p></div></div>
  <div class="service" style="left:780px;top:172px"><span class="service-icon"></span><div><h3>Group/Centre<br>Activities</h3><p>elementum elit at tellus nec ultricies sit amet porttitor</p></div></div>
  <div class="service" style="left:171px;top:370px"><span class="service-icon"></span><div><h3>Support<br>Coordination</h3><p>elementum elit at tellus nec ultricies sit amet porttitor mattis</p></div></div>
  <div class="service" style="left:470px;top:370px"><span class="service-icon"></span><div><h3>Innov Community<br>Participation</h3><p>elementum elit at tellus nec ultricies sit amet porttitor</p></div></div>
  <div class="service" style="left:780px;top:370px"><span class="service-icon"></span><div><h3>Home<br>Modification</h3><p>elementum elit at tellus nec ultricies sit amet porttitor</p></div></div>
  <a class="btn-outline">View more</a>
</section>

<svg class="services-bottom abs" width="1200" height="70" viewBox="0 0 1200 70">
  <rect width="1200" height="70" fill="var(--soft-bg)"/>
  <path d="M0 0 H1200 V8 C1000 30 800 40 600 32 C400 26 200 40 0 28Z" fill="var(--teal-deep)"/>
  <path d="M0 28 C200 40 400 26 600 32 C800 40 1000 30 1200 8 V20 C1000 44 800 56 600 48 C400 42 200 52 0 40Z" fill="var(--white)"/>
  <path d="M0 40 C200 52 400 42 600 48 C800 56 1000 44 1200 20 V30 C1000 60 800 66 600 60 C400 56 200 64 0 52Z" fill="var(--green)"/>
</svg>

<section class="blog abs">
  <h2>Recent Blog Posts</h2>
  <article class="post" style="left:176px">
    <div class="post-photo" role="img" aria-label="Photo of a carer with an elderly woman" style="background:linear-gradient(135deg,#c98a4a,#7c6a5a)"></div>
    <div class="post-date"><b>01</b><small>AUG</small></div>
    <h3>Your Blog Title here</h3>
    <p>netus et malesuada fames ac turpis egestas Cras id elit Integer quis urna Ut ante enim dapibus males</p>
    <a>READ MORE</a>
  </article>
  <article class="post" style="left:470px">
    <div class="post-photo" role="img" aria-label="Photo of a man in a wheelchair working at a desk" style="background:linear-gradient(135deg,#d8d6d0,#8d8a84)"></div>
    <div class="post-date"><b>01</b><small>AUG</small></div>
    <h3>Your Blog Title here</h3>
    <p>netus et malesuada fames ac turpis egestas Cras id elit Integer quis urna Ut ante enim dapibus males</p>
    <a>READ MORE</a>
  </article>
  <article class="post" style="left:763px">
    <div class="post-photo" role="img" aria-label="Photo of a wheelchair user boarding an accessible van" style="background:linear-gradient(135deg,#bfc3c6,#5a5f64)"></div>
    <div class="post-date"><b>01</b><small>AUG</small></div>
    <h3>Your Blog Title here</h3>
    <p>netus et malesuada fames ac turpis egestas Cras id elit Integer quis urna Ut ante enim dapibus males</p>
    <a>READ MORE</a>
  </article>
</section>

<footer class="site-footer abs">
  <div class="brand"><span class="brand-dot"></span><span class="brand-name">BrightHaven</span></div>
  <div class="footer-col" style="left:506px"><h4>Quick Links</h4><ul><li>Home</li><li>Services</li><li>About</li><li>Testimonials</li></ul></div>
  <div class="footer-col" style="left:670px"><h4>Resources</h4><ul><li>Why Us</li><li>Mission</li><li>Blog</li><li>Contact Us</li></ul></div>
  <div class="footer-col" style="left:825px">
    <h4>Follow Us</h4>
    <p class="signup-note">Please sign up here for update</p>
    <div class="signup"><span>Email address</span><span>›</span></div>
    <div class="socials"><span></span><span></span><span></span><span></span></div>
  </div>
</footer>

<div class="copyright abs">© 2018 Company Name&nbsp; All right reserved</div>

</body>
</html>
```